Industrial/Commercial Plumbing Capability Statement

Would like a construction capability statement/Brochure amended to be similar to the attached. -
Have included photos and Notes on the attached
would like project photos to be used
This is a previous capability statement that we would like amended and altered to include, safety, QA and Recent Projects
Please use our company logo
Updates

Need extra days to review

Target Market(s)

Construction work - Industrial

Industry/Entity Type

Plumbing

Requirements
Must have
• Include all items in contents page

Eye Catching Photos relevant to construction industry and relevant to topic on page

```html
<!DOCTYPE html>
<html lang="en">
<head>
<meta charset="utf-8">
<title>Norwell Plumbers – Capability Statement</title>
<link href="https://fonts.googleapis.com/css2?family=Montserrat:ital,wght@0,300;0,400;0,500;0,600;0,700;0,800;1,400;1,500&family=Oswald:wght@600&display=swap" rel="stylesheet">
<style>
:root{
  --navy:#0e3559;
  --navy-label:#1b4266;
  --white:#ffffff;
  --ink:#1f2f44;
  --accent:#d9d536;
  --board-top:#dfe8ee;
  --board:#a6b6c0;
}
*{box-sizing:border-box;margin:0;padding:0}
html,body{width:1200px;height:2983px;overflow:hidden}
body{
  position:relative;
  font-family:"Montserrat",sans-serif;
  background:linear-gradient(to bottom,var(--board-top) 0,#d3dee5 840px,var(--board) 840px,var(--board) 100%);
}
.board-label{
  position:absolute;
  font-family:"Montserrat",sans-serif;
  font-weight:400;
  font-size:54px;
  color:var(--navy-label);
  white-space:nowrap;
  transform:translate(-50%,-50%) rotate(-90deg);
  letter-spacing:1px;
}
.spread{
  position:absolute;
  overflow:hidden;
  background:var(--white);
  box-shadow:0 2px 6px rgba(0,0,0,.18);
}
.spread svg.shapes{position:absolute;left:0;top:0}
.abs{position:absolute}
.brand{
  position:absolute;
  font-family:"Montserrat",sans-serif;
  font-weight:800;
  font-size:19px;
  display:flex;align-items:center;gap:8px;
  letter-spacing:.3px;
  white-space:nowrap;
}
.brand .mark{width:14px;height:14px;display:inline-block;flex:none}
.rule{position:absolute;height:1px;background:var(--accent)}

/* cover */
.cover{left:171px;top:929px;width:857px;height:610px}
.front-brand{color:var(--navy);right:22px;top:34px}
.front-brand .mark{background:var(--navy)}
.cover-title{
  position:absolute;left:567px;top:430px;
  font-family:"Oswald",sans-serif;font-weight:600;
  font-size:64px;line-height:60px;color:var(--navy);
  white-space:nowrap;letter-spacing:-1px;
  transform:scale(.92,1.1);transform-origin:left top;
}
.back-brand{left:21px;top:486px;color:var(--white)}
.back-brand .mark{background:var(--white)}
.contact{left:21px;top:521px;color:var(--white);font-size:9.5px;line-height:15px}
.contact li{list-style:none;display:flex;align-items:center;gap:5px;white-space:nowrap}
.contact b{font-weight:700}
.contact svg{width:8px;height:9px}
.site{left:19px;top:571px;color:var(--white);font-size:15px;font-weight:500}

/* spread 2 */
.directors{left:162px;top:1594px;width:876px;height:621px}
.toc-title{left:21px;top:74px;color:var(--navy);font-size:18px;font-weight:600}
.toc{left:21px;top:119px;list-style:none}
.toc li{display:flex;align-items:baseline;height:36.3px;color:var(--navy)}
.toc .num{font-size:22px;font-weight:500;width:38px;letter-spacing:1px}
.toc .label{font-size:12.5px}
.tools-photo{left:165px;top:412px;width:300px;height:172px}
.section-title{font-size:21px;font-weight:300;letter-spacing:.3px;white-space:nowrap}
.section-title b{font-weight:700}
.msg-title{left:472px;top:40px;color:var(--white)}
.copy{font-size:7.4px;line-height:10.2px}
.msg{left:472px;top:77px;width:362px;color:#dfe7f0}
.msg .lead{font-size:12px;line-height:15px;font-weight:600;color:var(--white);margin:12px 0 12px}
.signature{position:absolute;width:92px;height:48px;top:462px;border-radius:3px}
.signer{position:absolute;top:528px;color:var(--white);font-size:14px;font-weight:300;white-space:nowrap}
.pg{position:absolute;font-size:9px}

/* spread 3 */
.about{left:162px;top:2264px;width:876px;height:622px}
.about-title{left:21px;top:40px;color:var(--navy)}
.about-copy{left:21px;top:80px;color:var(--ink)}
.about-copy p{margin-bottom:11px}
.quote-mark{left:460px;top:30px;color:var(--white);font-size:36px;font-weight:700}
.quote{left:498px;top:64px;width:334px;color:var(--white);font-style:italic;font-size:11.8px;line-height:14px;text-align:justify}
</style>
</head>
<body>

<span class="board-label" style="left:102px;top:1234px">COVER &amp; BACK</span>
<span class="board-label" style="left:1096px;top:1908px">PAGE 2 &amp; 3</span>
<span class="board-label" style="left:102px;top:2606px">Page 4 &amp; 5</span>

<!-- Cover & back -->
<section class="spread cover">
  <svg class="shapes" width="857" height="610" viewBox="0 0 857 610">
    <defs>
      <linearGradient id="coverSky" x1="0" y1="0" x2="0" y2="1">
        <stop offset="0" stop-color="#5067b5"/>
        <stop offset=".45" stop-color="#9fb1d4"/>
        <stop offset=".75" stop-color="#e3b77a"/>
        <stop offset="1" stop-color="#d7822f"/>
      </linearGradient>
    </defs>
    <polygon points="0,0 223,0 482,610 0,610" fill="var(--navy)"/>
    <polygon points="223,0 238,0 500,610 482,610" fill="#ffffff"/>
    <polygon points="238,0 857,0 857,610 500,610" fill="url(#coverSky)" role="img" aria-label="Photo of tower cranes over a construction site at sunset"/>
  </svg>
  <div class="brand front-brand"><span class="mark"></span>NORWELL PLUMBERS.</div>
  <h1 class="cover-title">CAPABILITY<br>STATEMENT</h1>
  <div class="rule" style="left:500px;top:581px;width:335px"></div>

  <div class="brand back-brand"><span class="mark"></span>NORWELL PLUMBERS.</div>
  <ul class="abs contact">
    <li><svg viewBox="0 0 8 10"><path d="M4 0a3.5 3.5 0 0 0-3.5 3.5C.5 6 4 10 4 10s3.5-4 3.5-6.5A3.5 3.5 0 0 0 4 0zm0 5a1.4 1.4 0 1 1 0-2.8A1.4 1.4 0 0 1 4 5z" fill="#fff"/></svg><span><b>Office:</b> 24 Hallam Rd, Westbury WA 6021</span></li>
    <li><svg viewBox="0 0 8 10"><path d="M4 0a3.5 3.5 0 0 0-3.5 3.5C.5 6 4 10 4 10s3.5-4 3.5-6.5A3.5 3.5 0 0 0 4 0zm0 5a1.4 1.4 0 1 1 0-2.8A1.4 1.4 0 0 1 4 5z" fill="#fff"/></svg><span><b>Postal address:</b> PO Box 3382, Westbury DC WA 6921</span></li>
    <li><svg viewBox="0 0 8 10"><path d="M1.6 .5 3 2.4 2.2 3.4c.6 1.4 1.5 2.4 2.7 3.1l1-.8L7.6 7l-.7 1.6C3.7 8.4.6 5 .8 1.3z" fill="#fff"/></svg><span>(08) 9000 4172</span></li>
  </ul>
  <div class="abs site">norwellplumbers.com.au</div>
  <div class="rule" style="left:210px;top:581px;width:270px"></div>
</section>

<!-- Pages 2 & 3 -->
<section class="spread directors">
  <svg class="shapes" width="876" height="621" viewBox="0 0 876 621">
    <defs>
      <linearGradient id="toolsTone" x1="0" y1="0" x2="1" y2="1">
        <stop offset="0" stop-color="#f1f2f4"/>
        <stop offset=".55" stop-color="#f6cf3a"/>
        <stop offset="1" stop-color="#e9ebee"/>
      </linearGradient>
    </defs>
    <polygon points="251,0 876,0 876,621 518,621" fill="var(--navy)"/>
  </svg>
  <h2 class="abs toc-title">Table of Content</h2>
  <ul class="abs toc">
    <li><span class="num">03</span><span class="label">From The Directors</span></li>
    <li><span class="num">04</span><span class="label">About The Business</span></li>
    <li><span class="num">06</span><span class="label">Our Services</span></li>
    <li><span class="num">07</span><span class="label">Health And Safety</span></li>
    <li><span class="num">08</span><span class="label">Quality Assurance</span></li>
    <li><span class="num">09</span><span class="label">Recent Projects</span></li>
    <li><span class="num">10</span><span class="label">Norwell Data</span></li>
    <li><span class="num">12</span><span class="label">Meet The Team</span></li>
  </ul>
  <svg class="abs tools-photo" viewBox="0 0 300 172" role="img" aria-label="Photo of a yellow hard hat, spirit level, tape measure and rolled building plans">
    <rect width="300" height="172" rx="8" fill="url(#toolsTone)"/>
  </svg>

  <h2 class="abs section-title msg-title">MESSAGE FROM THE <b>DIRECTORS</b></h2>
  <div class="abs msg copy">
    <p>Our modern day approach to Plumbing construction means that your Project benefits from the latest materials, techniques, and industry developments. As leaders in high quality construction Plumbing, commercial maintenance, and retail fit-outs, we stand at the forefront of Plumbing in Perth.</p>
    <p>Our innovative and dynamic approach to business places us ahead of our competition and showcases our skill and experience in delivering the right products and installation methods for your Projects.</p>
    <p class="lead">We work closely with our Builders on the scope of works, to guarantee that targets are met, and exceeded.</p>
    <p>Norwell Plumbers has extensive expertise across many areas, from new Shopping centres and Hospitals to industrial equipment.</p>
    <p>We constantly strive to exceed the expectations of our Customers and have a proven track record with the delivery of large-scale Projects, on time and on budget, and firmly believe that it is our job to make your Project a success and your experience positive.</p>
    <p class="lead">We pride ourselves on having the highest level of quality on-site management in the industry, displaying expert communication, effective collaboration and unmatched problem solving skills. We stand steadfast upon our reputation as problem solvers and innovative and flexible service providers.</p>
    <p>Norwell Plumbers believe with the proper team, you can avoid costly and unnecessary delays. When you work with us, you know that you are dealing with Perth's most trusted specialists in commercial Plumbing.</p>
    <p>We can't wait to start working with you.</p>
  </div>
  <div class="signature" style="left:560px;background:rgba(255,255,255,.06)" role="img" aria-label="Handwritten signature of Daniel Harte"></div>
  <div class="signature" style="left:688px;background:rgba(255,255,255,.06)" role="img" aria-label="Handwritten signature of Marco Bellini"></div>
  <span class="signer" style="left:564px">Daniel Harte</span>
  <span class="signer" style="left:688px">Marco Bellini</span>
  <div class="rule" style="left:46px;top:594px;width:789px"></div>
  <span class="pg" style="left:843px;top:589px;color:#fff">3</span>
</section>

<!-- Pages 4 & 5 -->
<section class="spread about">
  <svg class="shapes" width="876" height="622" viewBox="0 0 876 622">
    <defs>
      <linearGradient id="siteTone" x1="0" y1="0" x2="0" y2="1">
        <stop offset="0" stop-color="var(--navy)"/>
        <stop offset=".28" stop-color="#1d4a72"/>
        <stop offset=".48" stop-color="#8ea3b6"/>
        <stop offset=".75" stop-color="#b9b37a"/>
        <stop offset="1" stop-color="#6d7f8c"/>
      </linearGradient>
    </defs>
    <polygon points="269,0 382,0 631,622 518,622" fill="var(--navy)"/>
    <polygon points="382,0 391,0 640,622 631,622" fill="#ffffff"/>
    <polygon points="391,0 876,0 876,622 640,622" fill="url(#siteTone)" role="img" aria-label="Photo of a site worker in hard hat and hi-vis vest reviewing plans at a construction site"/>
  </svg>
  <h2 class="abs section-title about-title">ABOUT THE <b>BUSINESS</b></h2>
  <div class="abs about-copy copy">
    <p style="width:255px">Established in February 2004 by Managing Directors Marco Bellini and Daniel Harte, Norwell Plumbers specialises in the commercial sector and has extensive expertise in all levels of the industry, from new Shopping centres, Hotels, high-rise developments and Hospitals to industrial equipment in both construction and maintenance.</p>
    <p style="width:280px">Our relationships with our Suppliers is paramount to the success of our business and we have trading accounts with all major Plumbing Suppliers in Perth. We maintain working relationships with Manufacturers to ensure that we are the forefront of advancements within the Plumbing industry, both in products and Plumbing techniques.</p>
    <p style="width:300px">We strive for a balance in cost-effective Plumbing, whilst keeping the highest standards in the industry. We are relentless in our pursuit of quality and excellence in service. Our approach is built on collaboration, innovation, integrity and accountability - which underpin every interaction at each stage of the work we do. We focus on the relationships we build with our Customers, Colleagues, and Stakeholders to ensure the best outcomes.</p>
    <p style="width:325px">At Norwell Plumbers, we believe our excellent customer relations, passion about the industry and our expertise means we can deliver what we promise. We know this sets us apart as our satisfied Customers keep coming back, as well as recommending us to others and we believe this word of mouth speaks volumes.</p>
    <p style="width:350px">We know that our success, and success of our Projects, depends on the quality of our People. We are committed to attracting and retaining talented employees by providing a strong platform for ongoing career development. We recognise the value in every team member.</p>
    <p style="width:375px">We proudly employ a highly skilled team of full time staff ranging from fully qualified Trades people, Apprentices, and Administration Personnel. We are committed to the regular, ongoing training and cross-skilling of all our staff and promote a workplace culture that supports career advancement as well as professional and personal growth.</p>
  </div>
  <div class="abs quote-mark">&ldquo;</div>
  <p class="abs quote">As commercial Builders we often have to work on difficult Projects that require unique, innovative results. Norwell Plumbers are problem solvers and work closely with our team to deliver high quality solution oriented Projects. We started working with Norwell Plumbers several years ago and continue to be impressed by their professionalism and attention to detail</p>
  <div class="rule" style="left:38px;top:594px;width:790px"></div>
  <span class="pg" style="left:21px;top:589px;color:var(--navy)">4</span>
  <span class="pg" style="left:845px;top:589px;color:#fff">5</span>
</section>

</body>
</html>
```